Company selling food supplements with CBD needs label.

We need a label design for a company called "VEX Lab ltd", is based in the UK, the market name is "VEX" or "VEX Velvet Ember Xtracts". The initial product is Virgin Organic Hemp Seed Oil with a CBD in a 10ml amber dropper bottle. The design should be simplicity and luxury. The design should include also box.

Target Market(s)

Food supplements on Pellmart UK

Industry/Entity Type

Supplement

Font styles to use
Other font styles liked:
• Some luxury

Colors

Designer to choose colors to be used in the design.

Requirements
Must have
• All the information on the label required by the UK for the food supplements, the same on the box. One version matt one transparent. The design should include different CBD content, one different bottle (250mg, 500mg, 750mg, 1000mg) .
• The label and box should include the following phrases: "DIRECTIONS: Food Supplement. Shake well before use. Use 4-6 drops 2-3 times a day. Leave the oil in your mouth for 30-60 seconds before swallowing. Gradually build up the dose to find your optimum dosage.
• CAUTION: Do not exceed the recommended daily intake. Do not use as a substitute for a varied diet. Do not use during pregnancy and breastfeeding. Store in a dark and cool place, away from sunlight. Keep away from children.
• INGREDIENTS: Hemp Seed Oil, Omega-6 (2800mg), Omega-3 (930mg), CBD (250mg)
• MANUFACTURED: VEX Lab Ltd, 87 Quillon Rd, Harrow, KT9 4PW, www,vexlabuk.co.uk, info@vexlabuk.co.uk.
• EXPIRED DATE: "
• The box should also include a place for bark code.
Nice to have
• Simple and elegant design vertical or horizontal with exposed company logo "VEX" or "VEX Velvet Ember Xtracts". The company logo is provided but designers may change it freely.
Should not have
• The best without pictures/graphics overloading simplicity and purity of design.

```html
<!DOCTYPE html>
<html lang="en">
<head>
<meta charset="utf-8">
<title>VEX Virgin Organic Hemp Seed Oil CBD – Label and Box</title>
<link rel="stylesheet" href="https://fonts.googleapis.com/css2?family=Michroma&family=Oswald:wght@400&family=Marcellus&display=swap">
<style>
  :root {
    --stage: #e9e9e9;
    --paper: #f7f7f7;
    --ink: #111111;
    --gold-dark: #a8640c;
    --gold-mid: #e0a52a;
    --gold-light: #f2c23c;
    --gold-line: #d79a22;
    --band-text: #3a2408;
  }
  * { box-sizing: border-box; margin: 0; padding: 0; }
  html, body {
    width: 1200px; height: 848px; overflow: hidden;
    background: radial-gradient(ellipse at 50% 40%, #f6f6f6 0%, var(--stage) 70%, #dcdcdc 100%);
  }
  .canvas { position: relative; width: 1200px; height: 848px; }

  /* shared brand elements */
  .brand { text-align: center; color: var(--ink); }
  .brand-name {
    font-family: "Michroma", sans-serif;
    font-weight: 400;
    line-height: 1;
    letter-spacing: 0.02em;
  }
  .brand-tagline {
    font-family: "Oswald", sans-serif;
    font-weight: 400;
    letter-spacing: 0.01em;
  }
  .gold-band {
    background: linear-gradient(90deg, var(--gold-dark) 0%, var(--gold-mid) 22%, var(--gold-light) 50%, var(--gold-mid) 78%, var(--gold-dark) 100%);
    outline: 1px solid var(--gold-line);
    outline-offset: 3px;
    text-align: center;
    font-family: "Marcellus", serif;
    color: var(--band-text);
    text-transform: uppercase;
  }
  .product-code {
    font-family: "Marcellus", serif;
    text-align: center;
    color: var(--ink);
  }
  .volume {
    font-family: "Marcellus", serif;
    text-align: center;
    color: var(--ink);
  }
  .gold-rule { height: 3px; background: linear-gradient(90deg, var(--gold-dark), var(--gold-light), var(--gold-dark)); }

  /* bottle label */
  .bottle-label {
    position: absolute; left: 250px; top: 250px;
    width: 290px; height: 390px;
    background: var(--paper);
    box-shadow: 0 6px 24px rgba(0,0,0,0.12);
    display: flex; flex-direction: column; align-items: center;
  }
  .bottle-label .gold-rule.top { width: 100%; margin-top: 0; }
  .bottle-label .brand { margin-top: 30px; }
  .bottle-label .brand-name { font-size: 78px; }
  .bottle-label .brand-tagline { font-size: 19px; margin-top: 4px; }
  .bottle-label .gold-band {
    width: 250px; margin-top: 30px; padding: 8px 4px;
    font-size: 23px; line-height: 1.15;
  }
  .bottle-label .product-code { font-size: 52px; margin-top: 14px; }
  .bottle-label .gold-rule.bottom { width: 100%; margin-top: 10px; }
  .bottle-label .volume { font-size: 17px; margin-top: 6px; }
  .bottle-label .gold-rule.foot { width: 100%; margin-top: 6px; }

  /* box front panel */
  .box-front {
    position: absolute; left: 650px; top: 70px;
    width: 300px; height: 700px;
    background: linear-gradient(90deg, #f1f1f1 0%, var(--paper) 40%, #fbfbfb 100%);
    box-shadow: 0 8px 30px rgba(0,0,0,0.13);
    display: flex; flex-direction: column; align-items: center;
  }
  .box-front .gold-rule.top { width: 100%; margin-top: 10px; }
  .box-front .brand { margin-top: 90px; }
  .box-front .brand-name { font-size: 84px; }
  .box-front .brand-tagline { font-size: 21px; margin-top: 6px; }
  .box-front .gold-band {
    width: 272px; margin-top: 92px; padding: 18px 4px;
    font-size: 22px; line-height: 1.6; letter-spacing: 0.03em;
  }
  .box-front .product-code { font-size: 50px; margin-top: 26px; letter-spacing: 0.03em; }
  .box-front .drop-icon { margin-top: 94px; width: 62px; height: 96px; }
  .box-front .gold-rule.bottom { width: 100%; margin-top: auto; }
  .box-front .volume { font-size: 19px; margin: 10px 0; }
  .box-front .gold-rule.foot { width: 100%; margin-bottom: 14px; }
</style>
</head>
<body>
<main class="canvas">

  <section class="bottle-label" aria-label="Bottle label">
    <div class="gold-rule top"></div>
    <div class="brand">
      <div class="brand-name">VEX</div>
      <div class="brand-tagline">Velvet Ember Xtracts</div>
    </div>
    <div class="gold-band">Virgin Organic<br>Hemp Seed Oil</div>
    <div class="product-code">CBD</div>
    <div class="gold-rule bottom"></div>
    <div class="volume">10 ml</div>
    <div class="gold-rule foot"></div>
  </section>

  <section class="box-front" aria-label="Box front panel">
    <div class="gold-rule top"></div>
    <div class="brand">
      <div class="brand-name">VEX</div>
      <div class="brand-tagline">Velvet Ember Xtracts</div>
    </div>
    <div class="gold-band">Virgin Organic<br>Hemp Seed Oil</div>
    <div class="product-code">CBD</div>
    <svg class="drop-icon" viewBox="0 0 62 96" aria-hidden="true">
      <defs>
        <linearGradient id="dropGold" x1="0" y1="0" x2="1" y2="1">
          <stop offset="0" stop-color="#f2c23c"/>
          <stop offset="0.5" stop-color="#e0a52a"/>
          <stop offset="1" stop-color="#a8640c"/>
        </linearGradient>
      </defs>
      <path d="M31 2 C22 24 2 46 2 64 A29 30 0 0 0 60 64 C60 46 40 24 31 2 Z" fill="url(#dropGold)"/>
      <path d="M31 14 C24 32 9 50 9 65 A22 23 0 0 0 53 65 C53 50 38 32 31 14 Z" fill="#1b1b1b"/>
    </svg>
    <div class="gold-rule bottom"></div>
    <div class="volume">10 ml</div>
    <div class="gold-rule foot"></div>
  </section>

</main>
</body>
</html>
```